Bref créative
Bridgewell Brochure
Brochure
The brochure I want is a double-sided, tri-fold, 8.5" x 11". I have uploaded a sketch on what I would like on each side, as well as my original brochure. I will describe what I want on each side, and each section.
Inside (refer to formatting of original brochure):
left -- I want this section to be very similar to the original, but with a new design consistent with our colors and logo. Attached is a file titled "Bridgewell Brochure -- NEW TEXT" that is the new text I want in the section.
middle -- I want the text of the original brochure to remain the same, but consistent with new design/colors, and also if we can use our logo's "cube" as the new separator between the testimonials.
right -- I want this to be all new (not like original), with the text, "Visit us on the web at: www.BridgewellHoldingsNY.example" and below that, the text, "find our Attorney tab". The designer is open to design this section any way they would like, consistent with the overall design.
Outside (refer to formatting of original brochure):
left -- this section can be just like the original brochure, just with the updated design. I still want 'scales of justice' included in this section.
middle -- same as original brochure, just with our new address: 418 Maplecrest Avenue, Floral Park, NY 11001
right -- same as original brochure, just with new design
On the whole, I am looking for a design that is a little more sleek, modern, and simple. I would urge the designers to please stay away from swirly text or design features.
Real Estate
attorneys and businessmen
I have uploaded both sides of our old brochure. We want something nearly identical, just more reflective of our colors and style.
I have also uploaded our logo, business card, and new text for the left side of the inside of the brochure.
Lastly, I am uploading a new mock-up of the 6 sections of the brochure (similar to old version).
ANY SUBMISSION THAT DEVIATES TOO MUCH FROM OUR PREVIOUS DESIGN WILL BE IMMEDIATELY ELIMINATED.

```html
<!DOCTYPE html>
<html lang="en">
<head>
<meta charset="utf-8">
<title>Bridgewell Asset Management – Tri-fold Brochure</title>
<link href="https://fonts.googleapis.com/css2?family=Libre+Baskerville:ital,wght@0,400;0,700;1,400&family=Lora:ital,wght@0,400;0,600;1,400&display=swap" rel="stylesheet">
<style>
:root{
  --navy:#262b66;
  --purple:#3d3282;
  --gold:#c9a23a;
  --ink:#3c3c44;
  --muted:#7a7a86;
  --paper:#ffffff;
  --stage:#e6e4e0;
  --head:"Libre Baskerville", Georgia, serif;
  --body:"Lora", Georgia, serif;
}
*{box-sizing:border-box;margin:0;padding:0}
html,body{width:1200px;height:1062px;overflow:hidden;background:var(--stage)}
.canvas{width:1200px;height:1062px;display:flex;flex-direction:column;align-items:center;justify-content:center;gap:20px}
.sheet{width:648px;height:501px;background:var(--paper);display:flex;position:relative;box-shadow:0 2px 10px rgba(0,0,0,.18);overflow:hidden}
.panel{width:216px;height:100%;position:relative;padding:16px 14px 0;font-family:var(--body);color:var(--ink);font-size:7.2px;line-height:1.45}
.panel + .panel{border-left:1px dashed #ececf0}
.band{position:absolute;left:0;right:0;bottom:0;height:26px;background:var(--navy);border-top:3px solid var(--gold)}
.band.thin{height:14px}
h2{font-family:var(--head);font-weight:700;color:var(--navy);font-size:13px;display:flex;align-items:center;gap:6px;border-bottom:1px solid var(--gold);padding-bottom:3px;margin-bottom:7px}
.cube{width:11px;height:11px;flex:none}
ul.bullets{list-style:none;margin:6px 0 0 8px}
ul.bullets li{font-size:8px;padding-left:10px;position:relative;margin-bottom:3px;font-style:italic}
ul.bullets li::before{content:"";position:absolute;left:0;top:3px;width:5px;height:5px;background:var(--gold)}
.art{background:linear-gradient(160deg,#f2efe6,#d9cfae);border-radius:2px}
.tollfree{position:absolute;left:14px;bottom:40px;font-family:var(--head);color:var(--navy)}
.tollfree small{display:block;font-size:9px}
.tollfree strong{font-size:19px;font-weight:700}
.return-address{position:absolute;right:18px;top:16px;writing-mode:vertical-rl;font-family:var(--head);font-size:9px;line-height:1.5;color:var(--navy)}
.return-address strong{font-weight:700}
.envelope{position:absolute;left:18px;right:58px;top:150px;height:170px;background:linear-gradient(160deg,#fbfbfb,#e2e2e7);border:1px solid #e6e6ea}
.web-strip{position:absolute;left:0;right:0;bottom:34px;text-align:center;font-family:var(--head);font-size:7.5px;color:var(--navy);letter-spacing:.5px}
.brand{display:flex;align-items:center;gap:6px;margin:28px 0 0 10px}
.brand-mark{width:14px;height:14px;background:var(--gold)}
.brand-name{font-family:var(--head);color:var(--navy);font-size:14px;line-height:1.1;font-weight:400}
.brand-name small{display:block;font-size:7.5px;letter-spacing:1.5px}
.tagline{font-family:var(--head);color:var(--navy);font-size:17px;line-height:1.25;margin:56px 0 0 22px;font-style:italic}
.tagline span{font-style:normal}
.swoosh{position:absolute;left:0;bottom:26px;width:216px;height:40px}
p{margin-bottom:6px;text-align:justify}
.faint-word{position:absolute;left:14px;bottom:34px;font-family:var(--head);font-size:22px;color:#e9e9ee;letter-spacing:1px}
.quote{font-style:italic;margin-bottom:3px}
.sig{text-align:right;font-size:7px;color:var(--muted);margin-bottom:2px}
.sep{display:flex;justify-content:center;margin:5px 0}
.photo{height:110px;margin:0 0 8px;background:linear-gradient(160deg,#d8d8de,#8c8ea0)}
.visit{text-align:center;font-family:var(--head);color:var(--navy)}
.visit b{font-size:10px;display:block}
.visit .url{font-size:7.5px;display:block;margin:2px 0}
.visit em{font-size:7px;color:var(--gold)}
.services{list-style:none;margin-left:6px}
.services li{font-size:7.5px;padding-left:9px;position:relative;margin-bottom:2px}
.services li::before{content:"";position:absolute;left:0;top:3px;width:4px;height:4px;background:var(--gold)}
.lead{font-style:italic;margin-bottom:4px}
.gap-top{margin-top:10px}
</style>
</head>
<body>
<main class="canvas">
  <section class="sheet outside">
    <div class="panel panel-offering">
      <h2><svg class="cube" viewBox="0 0 12 12"><rect width="12" height="12" fill="var(--gold)"/></svg>Offering</h2>
      <ul class="bullets">
        <li>Prompt Professional Service</li>
        <li>Immediate Closings</li>
        <li>Investor Purchases</li>
        <li>Honesty &amp; Integrity</li>
      </ul>
      <div class="art" role="img" aria-label="Scales of justice" style="width:110px;height:130px;margin:22px 0 0 6px"></div>
      <div class="tollfree"><small>Toll Free</small><strong>1-800-555-0142</strong></div>
      <div class="band thin"></div>
    </div>
    <div class="panel panel-mailer">
      <address class="return-address" style="font-style:normal">
        <strong>Bridgewell Equities Inc.</strong>
        <span>418 Maplecrest Avenue</span>
        <span>Floral Park, NY 11001</span>
      </address>
      <div class="envelope" role="img" aria-label="Blank mailing envelope"></div>
      <div class="web-strip">www.BridgewellHoldingsNY.example</div>
      <div class="band thin"></div>
    </div>
    <div class="panel panel-cover">
      <div class="brand"><span class="brand-mark"></span><div class="brand-name">BRIDGEWELL<small>ASSET MANAGEMENT</small></div></div>
      <div class="tagline"><span>Providing</span><br>Solutions<br>for<br>you and your<br>Clients</div>
      <svg class="swoosh" viewBox="0 0 216 40" preserveAspectRatio="none"><path d="M0 40 C70 10 150 8 216 26 L216 40 Z" fill="var(--purple)"/><path d="M0 36 C70 6 150 4 216 22" stroke="var(--gold)" stroke-width="2" fill="none"/></svg>
      <div class="band"></div>
    </div>
  </section>

  <section class="sheet inside">
    <div class="panel panel-results">
      <h2><svg class="cube" viewBox="0 0 12 12"><rect width="12" height="12" fill="var(--gold)"/></svg>Driven by Results</h2>
      <p>Bridgewell Asset Management has established itself as a premier investment consortium specializing in the purchase of properties in distressed situations, so doing just that to make it simpler for you and your clients to move forward with confidence and care.</p>
      <p>Our experienced team works directly with homeowners, attorneys, and real estate brokers to find practical answers that fit each unique property and schedule.</p>
      <h2 class="gap-top"><svg class="cube" viewBox="0 0 12 12"><rect width="12" height="12" fill="var(--gold)"/></svg>When a swift closing is needed...</h2>
      <p>Bridgewell steps in with ready capital, clear terms, and a reliable process from first call to final signing. Our reputation rests on keeping every promise we make to sellers and partners.</p>
      <div class="faint-word">RELIABILITY</div>
      <div class="band thin"></div>
    </div>
    <div class="panel panel-testimonials">
      <h2><svg class="cube" viewBox="0 0 12 12"><rect width="12" height="12" fill="var(--gold)"/></svg>Don't just take our word for it.</h2>
      <p class="lead">Hear what our critics have to say</p>
      <p class="quote">"I have had the pleasure of closing with Bridgewell several times. Their team is honest, fast, and always ready to help."</p>
      <div class="sig">Irene Vale, Attorney at Law</div>
      <div class="sep"><svg width="12" height="12"><rect width="12" height="12" fill="var(--gold)"/></svg></div>
      <p class="quote">"Closings were handled smoothly and on time. Everyone involved felt respected throughout the process."</p>
      <div class="sig">Dorian Pell, Broker</div>
      <div class="sep"><svg width="12" height="12"><rect width="12" height="12" fill="var(--gold)"/></svg></div>
      <p class="quote">"Bridgewell brings diligence and clear answers. Their commitment makes a difficult sale far easier for clients."</p>
      <div class="sig">Nora Fenwick, Attorney at Law</div>
      <div class="band thin"></div>
    </div>
    <div class="panel panel-visit">
      <div class="photo art" role="img" aria-label="Handshake passing house keys"></div>
      <div class="visit"><b>COME !! Visit Us At</b><span class="url">www.BridgewellHoldingsNY.example</span><em>find our Attorney tab</em></div>
      <h2 style="margin-top:12px"><svg class="cube" viewBox="0 0 12 12"><rect width="12" height="12" fill="var(--gold)"/></svg>Services</h2>
      <p class="lead">We offer a wide range of services:</p>
      <ul class="services">
        <li>Property management</li>
        <li>Purchase of non-performing notes</li>
        <li>REO support</li>
        <li>Foreclosure</li>
        <li>Quality acquisitions and repairs</li>
        <li>Property consultation</li>
        <li>Estate related issues</li>
        <li>Legal counsel</li>
      </ul>
      <div class="band"></div>
    </div>
  </section>
</main>
</body>
</html>
```